Word Press Website design

Vantor Webworks is a Website design, SEO, Social Networking and app development company. We would like to see what you can do to create a new, relevant and exciting design for us. This is our first project for Pixel Bazaar so we thought we would test drive this site.  We would like to leave it up to your creative interpretation of the new design, but you can checkout our old design at www.vantorwebcrafters.com
We are always looking for new talent for future projects. Wow us with your designs and there will be future work for you.

Target Market(s)
Our target customers are medium sized businesses of all vertical markets.
Industry/Entity Type
Internet
Requirements
Must have
- Easy to navigate, HTML 5 sliders, modern
Nice to have
- Bring your graphic talents with an outside of the box design that will standout to prospective clients.

```html
<!DOCTYPE html>
<html lang="en">
<head>
<meta charset="utf-8">
<title>Vantor Webworks</title>
<link href="https://fonts.googleapis.com/css2?family=Montserrat:wght@400;600;700&family=Open+Sans:wght@400;600;700&display=swap" rel="stylesheet">
<style>
:root{
  --ink:#222;
  --muted:#777;
  --accent:#e0402a;
  --topbar:#f4f4f4;
  --line:#e4e4e4;
  --gold:#c98a3a;
  --dark:#3a3a3a;
  --footer:#262626;
  --footer-deep:#141414;
  --white:#fff;
}
*{box-sizing:border-box;margin:0;padding:0}
html,body{width:1200px;height:2194px;overflow:hidden}
body{font-family:"Open Sans",Arial,sans-serif;color:var(--ink);background:var(--white);position:relative}
.abs{position:absolute}
.topbar{left:0;top:0;width:1200px;height:40px;background:var(--topbar);border-bottom:1px solid var(--line)}
.social{left:232px;top:13px;display:flex;gap:22px}
.social span{width:12px;height:12px;border-radius:50%;background:#bdbdbd;display:block}
.contact-info{left:590px;top:12px;display:flex;gap:34px;font-size:10px;color:#999}
.contact-info span::before{content:"";display:inline-block;width:8px;height:8px;border-radius:50%;background:#c8c8c8;margin-right:7px;vertical-align:-1px}
.header{left:0;top:40px;width:1200px;height:74px;background:var(--white)}
.logo{left:220px;top:52px;display:flex;align-items:center;gap:10px}
.logo-mark{width:40px;height:40px;border-radius:50%;background:var(--ink)}
.logo-name{font-family:"Montserrat",sans-serif;font-weight:700;font-size:17px;line-height:19px;color:var(--ink);width:90px}
.nav{left:538px;top:70px;display:flex;gap:36px;font-family:"Montserrat",sans-serif;font-size:11px;font-weight:600;color:#333}
.nav .active{color:var(--accent)}
.hero{left:0;top:114px;width:1200px;height:364px;background:linear-gradient(100deg,#d9d2c6 0%,#b39678 35%,#8a5a2c 60%,#6b3f1b 100%)}
.hero-text{left:562px;top:218px;width:430px;color:var(--white)}
.hero-text h1{font-family:"Montserrat",sans-serif;font-size:15px;font-weight:700;margin-bottom:18px}
.hero-text p{font-size:16px;line-height:20px;margin-bottom:18px;font-weight:600}
.quote-band{left:0;top:478px;width:1200px;height:82px;background:linear-gradient(90deg,#d39a4e,#b67a34)}
.quote-band h2{position:absolute;left:219px;top:28px;font-family:"Montserrat",sans-serif;font-size:19px;font-weight:700;color:#1c1c1c}
.btn{display:inline-block;background:#111;color:var(--white);font-family:"Montserrat",sans-serif;font-weight:600;text-align:center;border-radius:4px}
.quote-band .btn{position:absolute;left:838px;top:22px;width:140px;height:38px;line-height:38px;font-size:14px}
.service{top:588px;width:243px}
.service .photo{height:125px;background:linear-gradient(135deg,#cfd4d8,#7f8a92)}
.service h3{font-size:11px;font-weight:700;margin-top:13px}
.service .sub{font-size:12px;color:var(--muted);margin-top:3px}
.service p{font-size:11px;line-height:18px;margin-top:4px;color:#333}
.clients{left:0;top:845px;width:1200px;height:296px;background:var(--dark)}
.clients h2{position:absolute;left:0;width:1200px;top:30px;text-align:center;color:var(--white);font-family:"Montserrat",sans-serif;font-size:24px;font-weight:700;letter-spacing:1px}
.thumb{top:76px;width:240px;height:191px}
.thumb.hover{background:#c1924f;display:flex;align-items:center;justify-content:center;color:var(--white);font-family:"Montserrat",sans-serif;font-weight:700;font-size:24px;text-align:center;line-height:30px}
.offer-tabs{left:219px;top:1178px;width:88px;text-align:right;font-size:12px}
.offer-tabs li{list-style:none;height:33px;line-height:22px;color:#333;padding-right:0}
.offer-tabs li.current{border-left:4px solid var(--ink);padding-left:14px;text-align:left}
.offer{left:347px;top:1178px;width:358px}
.offer h3{font-family:"Montserrat",sans-serif;font-size:12px;font-weight:700;margin-bottom:18px}
.offer ul{list-style:none;font-size:10px}
.offer li{height:28px;display:flex;align-items:flex-start;gap:10px}
.offer li svg{flex:none}
.offer p{font-size:10px;line-height:15px;color:#888}
.consult{left:739px;top:1178px;width:246px}
.consult .photo{height:121px;background:linear-gradient(120deg,#e7e4df,#8f8a84 60%,#4a4642)}
.consult h3{font-family:"Montserrat",sans-serif;font-size:12px;font-weight:700;margin-top:12px}
.consult p{font-size:10px;line-height:15px;color:#888;margin-top:6px}
.idea{left:0;top:1448px;width:1200px;height:213px;background:linear-gradient(90deg,#1d1d1d,#3b3b3b 50%,#262626)}
.idea h2{position:absolute;left:0;width:1200px;top:68px;text-align:center;color:var(--white);font-family:"Montserrat",sans-serif;font-size:23px;font-weight:700}
.idea .btn{position:absolute;left:534px;top:115px;width:130px;height:32px;line-height:32px;font-size:12px;border-radius:3px}
.trust h2{position:absolute;left:0;width:1200px;top:1693px;text-align:center;font-family:"Montserrat",sans-serif;font-size:14px;font-weight:600}
.trust-line{left:300px;top:1760px;width:600px;border-top:1px solid var(--line)}
.trust-logos{left:300px;top:1776px;width:600px;display:flex;justify-content:space-between;font-family:"Open Sans",sans-serif;font-weight:600;font-size:17px;color:#333}
.trust-line.low{top:1810px}
.trust-note{left:0;width:1200px;top:1818px;text-align:center;font-size:13px;color:#bbb}
.footer{left:0;top:1891px;width:1200px;height:255px;background:var(--footer);color:var(--white)}
.footer h4{font-family:"Montserrat",sans-serif;font-size:12px;font-weight:700;margin-bottom:18px}
.fcol{top:1931px;font-size:10px}
.fcol li{list-style:none;line-height:24px}
.f-about .mark{width:44px;height:44px;border-radius:50%;background:var(--white);margin:0 0 6px 40px}
.f-about .name{font-family:"Montserrat",sans-serif;font-weight:700;font-size:12px;margin-bottom:6px;padding-left:12px}
.f-about p{width:170px;line-height:14px;font-size:10px}
.tags{display:flex;flex-wrap:wrap;gap:8px;width:160px}
.tags span{background:#3a3a3a;padding:5px 12px;font-size:9px}
.bottom{left:0;top:2146px;width:1200px;height:48px;background:var(--footer-deep);color:#aaa;font-size:9px;text-align:center;line-height:48px}
</style>
</head>
<body>
<div class="abs topbar"></div>
<div class="abs social"><span></span><span></span><span></span><span></span></div>
<div class="abs contact-info"><span>Mon - Sat 7:00 - 17:00</span><span>+ 1 555 010 2040</span><span>hello@vantorwebworks.com</span></div>

<div class="abs header"></div>
<div class="abs logo"><div class="logo-mark"></div><div class="logo-name">Vantor Webworks</div></div>
<nav class="abs nav"><span class="active">HOME</span><span>PROJECTS</span><span>WHAT WE DO</span><span>ABOUT US</span><span>BLOG</span><span>CONTACT US</span>
<svg width="12" height="12" viewBox="0 0 12 12"><circle cx="5" cy="5" r="3.5" fill="none" stroke="#333" stroke-width="1.6"/><line x1="7.6" y1="7.6" x2="11" y2="11" stroke="#333" stroke-width="1.8"/></svg></nav>

<div class="abs hero" role="img" aria-label="Close-up photo of a keyboard and eyeglasses on a warm wooden desk"></div>
<div class="abs hero-text">
  <h1>KANSAS CITY WEBSITE DESIGN - VANTOR WEBWORKS, L.L.C.</h1>
  <p>Do you want us to tell you the truth about <b>Vantor Webworks</b>, or tell you what you want to hear?</p>
  <p>Just the facts then: Vantor Webworks invented the Internet...it is even named after us! Ok...truth is, <b>Vantor Webworks</b> has a long history of building high performance Websites.</p>
</div>

<div class="abs quote-band"><h2>GET IN TOUCH TODAY FOR A FREE QUOTE</h2><span class="btn">CONTACT US</span></div>

<article class="abs service" style="left:217px"><div class="photo" role="img" aria-label="Photo of hands typing on a laptop"></div><h3>TITLE OF SERVICE 1</h3><div class="sub">SUBTITLE</div><p>This is some text that can be used to explain the service a bit more.</p></article>
<article class="abs service" style="left:478px"><div class="photo" role="img" aria-label="Photo of a desk with notebook, glasses and plant"></div><h3>TITLE OF SERVICE 3</h3><div class="sub">SUBTITLE</div><p>This is some text that can be used to explain the service a bit more.</p></article>
<article class="abs service" style="left:739px"><div class="photo" role="img" aria-label="Photo of a laptop on a desk by a window"></div><h3>TITLE OF SERVICE 3</h3><div class="sub">SUBTITLE</div><p>This is some text that can be used to explain the service a bit more.</p></article>

<section class="abs clients">
  <h2>OUR CLIENTS</h2>
  <div class="abs thumb" style="left:0;background:linear-gradient(135deg,#d8cfc0,#8a7a62)" role="img" aria-label="Client website screenshot: furniture store"></div>
  <div class="abs thumb hover" style="left:240px">HOVER OVER<br>EXAMPLE</div>
  <div class="abs thumb" style="left:480px;background:linear-gradient(180deg,#e8ecf2,#7f9bb8)" role="img" aria-label="Client website screenshot: utility billing"></div>
  <div class="abs thumb" style="left:720px;background:linear-gradient(135deg,#dfe8a8,#a9bd3c)" role="img" aria-label="Client website screenshot: scent shop"></div>
  <div class="abs thumb" style="left:960px;background:linear-gradient(180deg,#f1f1f1,#9c9c9c)" role="img" aria-label="Client website screenshot: parking technology"></div>
</section>

<ul class="abs offer-tabs">
  <li class="current">Web Design</li><li>SEO</li><li>Hosting</li><li>eCommerce</li><li>Programming</li><li>Photography</li>
</ul>
<div class="abs offer">
  <h3>WHAT WE OFFER</h3>
  <ul>
    <li><svg width="10" height="10" viewBox="0 0 10 10"><rect x=".5" y=".5" width="9" height="9" fill="none" stroke="#333"/><path d="M2 5l2 2 4-4" fill="none" stroke="#333" stroke-width="1.4"/></svg>Great Services</li>
    <li><svg width="10" height="10" viewBox="0 0 10 10"><rect x=".5" y=".5" width="9" height="9" fill="none" stroke="#333"/><path d="M2 5l2 2 4-4" fill="none" stroke="#333" stroke-width="1.4"/></svg>Great Services</li>
    <li><svg width="10" height="10" viewBox="0 0 10 10"><rect x=".5" y=".5" width="9" height="9" fill="none" stroke="#333"/><path d="M2 5l2 2 4-4" fill="none" stroke="#333" stroke-width="1.4"/></svg>Great Services</li>
  </ul>
  <p>Lorem ipsum dolor sit amet, consectetur adipiscing elit. Quisque nec erat erat. Integer blandit, nulla quis fermentum hendrerit, nisi diam viverra metus, porta semper est ipsum at sapien.<br>Suspendisse eget felis eget nulla placerat luctus id quis sapien. Sed metus felis, euismod at euismod et, feugiat viverra lacus tortor at quisque nec erat.</p>
</div>
<div class="abs consult">
  <div class="photo" role="img" aria-label="Photo of a person working on a tablet"></div>
  <h3>GET YOUR FREE CONSULTING</h3>
  <p>Have an idea, a dream? We can make it happen. Join our family, we offer free consultation to achieve your goals with creativity and quality that you deserve.</p>
</div>

<section class="abs idea" role="img" aria-label="Dark photo of a person at a desk">
  <h2>FROM IDEA, PLAN TO FINAL SOLUTION</h2>
  <span class="btn">GET IN TOUCH</span>
</section>

<section class="trust"><h2>CLIENTS THAT TRUST US</h2></section>
<div class="abs trust-line"></div>
<div class="abs trust-logos"><span>Framewell</span><span>Stonera</span><span>TALLMASON</span><span>Northpeak</span><span>Brightline</span></div>
<div class="abs trust-line low"></div>
<div class="abs trust-note">some of our clients that trust us, be shure to be one of them</div>

<footer class="abs footer"></footer>
<div class="abs fcol f-about" style="left:219px"><h4>ABOUT US</h4><div class="mark"></div><div class="name">Vantor Webworks</div><p>Lorem ipsum dolor sit amet, consectetur adipiscing elit. Nam turpis quam, sodales in ante sagittis, varius efficitur mauris.</p></div>
<div class="abs fcol" style="left:415px"><h4>NAVIGATION</h4><ul><li><b>Home</b></li><li>Projects</li><li>What we do</li><li>About us</li><li>Blog</li><li>Contact us</li></ul></div>
<div class="abs fcol" style="left:610px"><h4>TAGS</h4><div class="tags"><span>big</span><span>buildings</span><span>home</span><span>modern</span><span>simple</span></div></div>
<div class="abs fcol" style="left:805px"><h4>OUR RECENT PROJECTS</h4><ul><li>Modern Building</li><li>Interior Concept</li><li>Corporate concept</li><li>Corporate Tower</li><li>Sea side residence</li></ul></div>
<div class="abs bottom">copyright vantor 2015</div>
</body>
</html>
```